Coach/consultant in conflict and challenge needs an enticing flyer

I need a double sided DL flyer design that will describe my work in helping people meet conflict and emotional challenge so they can learn and grow from these difficulties. I want to give a flavour of my style through fresh colours, repeated images used differently (the spiral), and a sense of positivity around conflict and difficulty. I want to attract people who are keen to do things differently and want to engage with creative processes rather than getting stuck in familiar patterns. My work is creative and often includes use of story, images and fables, so I want to convey that as well. I also place the work in a spiritual context, but grounded in practicality so I don't want it to seem New Age or flakey. I want something that seems innovative, professional and intriguing. I've included a sample of something I mocked up in word and also a copy of a flyer for Marla Quennet's Ember Gathering that inspired me to get a DL flyer. I want the design to communicate trust and transformation and engaging with fresh ways of doing things by moving past old habits

Target Market(s)

Mid 30s plus women and men who want to change their approach to conflict and emotional difficulties and are willing to take the creative and challenging journey to do that

Industry/Entity Type

Learn

Colors
acd136
00a990

Requirements
Must have
• a shift in the use of the spiral image,
• use of image of me (Norah)
• bright fresh colours olours that represent growth and transformation--I've suggested lime green as it suggests a sense of growth
• easy to read text
Nice to have
• Interesting non-traditional fonts perhaps text in a contemporary sans serif and another brush script font (like the Ember Gathering example)
• bleed to the edge and run off the page images or text
Should not have
• anything that represents too much tradition or stuckness

```html
<!DOCTYPE html>
<html lang="en">
<head>
<meta charset="utf-8">
<title>Norah Ashford – DL Flyer</title>
<link rel="stylesheet" href="https://fonts.googleapis.com/css2?family=Open+Sans:wght@400;600;700&display=swap">
<style>
  :root{
    --teal:#00a990;
    --teal-soft:#3dbfa8;
    --lime:#acd136;
    --lime-deep:#7fb32c;
    --lime-pale:#d6eaa0;
    --cream:#fffdf0;
    --white:#ffffff;
    --ink-teal:#0f9b85;
  }
  *{box-sizing:border-box;margin:0;padding:0}
  html,body{width:1200px;height:1000px;overflow:hidden;background:#fff}
  body{position:relative;font-family:"Open Sans",Arial,sans-serif}
  .flyer-side{position:absolute;left:122px;width:959px;height:452px;overflow:hidden;
    background:
      radial-gradient(ellipse 60% 40% at 60% 45%, rgba(240,250,210,.85), rgba(240,250,210,0) 70%),
      linear-gradient(160deg,#cfe58a 0%,var(--lime) 45%,var(--lime-deep) 100%);}
  .side-front{top:36px}
  .side-back{top:507px;
    background:
      radial-gradient(ellipse 55% 45% at 65% 30%, rgba(235,248,200,.8), rgba(235,248,200,0) 70%),
      linear-gradient(170deg,var(--lime) 0%,#8cc63f 55%,#4fb86a 100%);}
  .diagonal-art{position:absolute;inset:0;width:959px;height:452px}
  .portrait-photo{position:absolute;inset:0;
    clip-path:polygon(0 0,455px 0,70px 452px,0 452px);
    background:
      radial-gradient(ellipse 30% 28% at 22% 40%, #d9b8a0 0%, rgba(217,184,160,0) 100%),
      radial-gradient(ellipse 40% 35% at 20% 25%, #7d736a 0%, rgba(125,115,106,0) 100%),
      linear-gradient(180deg,#9aa08a 0%,#a89582 50%,#c8502a 80%,#b8441f 100%);}
  .name-mark{position:absolute;left:30px;top:125px;color:var(--cream);line-height:1}
  .name-mark .first{display:block;font-size:70px;font-weight:400;letter-spacing:-1px}
  .name-mark .last{display:block;font-size:52px;font-weight:700;margin-top:4px}
  .tag-bar{position:absolute;left:273px;top:74px;width:640px;height:62px;border-radius:24px 0 0 24px;
    background:linear-gradient(90deg,rgba(190,225,90,.95),rgba(190,225,90,0) 95%);
    border-top:3px solid rgba(220,150,120,.6)}
  .tags{position:absolute;color:var(--white);font-weight:700;white-space:nowrap;
    text-shadow:0 2px 3px rgba(0,80,40,.45)}
  .tags-front{left:307px;top:82px;font-size:32px;word-spacing:4px}
  .tags-back{left:234px;top:282px;font-size:25px;word-spacing:4px}
  .lead{position:absolute;left:331px;top:173px;width:580px;font-size:20.5px;line-height:1.3;color:var(--ink-teal)}
  .about{position:absolute;left:295px;top:310px;width:620px;font-size:19.5px;line-height:1.45;font-weight:700;color:var(--white)}
  .body-copy{position:absolute;color:var(--white);font-size:15.6px;line-height:1.4;text-align:justify}
  .copy-consult{left:436px;top:43px;width:486px}
  .copy-experience{left:320px;top:195px;width:602px}
  .credential-box{position:absolute;left:70px;top:340px;width:405px;height:76px;border-radius:0 22px 22px 22px;
    background:var(--teal);box-shadow:5px 5px 0 var(--lime-deep);color:var(--white);padding:6px 0 0 32px}
  .credential-box .name{font-size:25px;line-height:1.2}
  .credential-box .name b{font-size:22px}
  .credential-box .quals{font-size:16.5px}
  .contact{position:absolute;left:561px;top:343px;color:var(--white);font-size:16.5px;line-height:1.3}
</style>
</head>
<body>

<section class="flyer-side side-front">
  <svg class="diagonal-art" viewBox="0 0 959 452" aria-hidden="true">
    <defs>
      <linearGradient id="tealPanel" x1="0" y1="0" x2="1" y2="1">
        <stop offset="0" stop-color="#1f9e88"/>
        <stop offset="1" stop-color="#4cc3ac"/>
      </linearGradient>
    </defs>
    <polygon points="0,0 458,0 63,452 0,452" fill="url(#tealPanel)"/>
    <polygon points="445,0 462,0 72,452 60,452" fill="#bfe7d8" opacity=".8"/>
    <polygon points="462,0 470,0 80,452 72,452" fill="#4db89a" opacity=".7"/>
  </svg>
  <h1 class="name-mark"><span class="first">Norah</span><span class="last">Ashford</span></h1>
  <div class="tag-bar"></div>
  <p class="tags tags-front"># courage &nbsp;# listening # creativity</p>
  <p class="lead">Challenge, change and conflict are a natural part of life. When we greet them with courage, and listen to what they tell us, we grow in wisdom, resilience and creativity.</p>
  <p class="about">Norah Ashford is a coach, educator and mediator. She works with people who want to harvest the fruits of challenge and conflict so they live life differently.</p>
</section>

<section class="flyer-side side-back">
  <div class="portrait-photo" role="img" aria-label="Portrait photograph of Norah Ashford"></div>
  <svg class="diagonal-art" viewBox="0 0 959 452" aria-hidden="true">
    <polygon points="445,0 462,0 77,452 62,452" fill="#e4f3c0" opacity=".85"/>
    <polygon points="462,0 472,0 87,452 77,452" fill="#3fae86" opacity=".75"/>
  </svg>
  <p class="body-copy copy-consult">Consult with Norah to address challenges in your life, relationship, group or organisation. Through listening, conversation and creative processes, you will discover what your challenge is asking of you. Norah Ashford is a skilled facilitator who works to shift people’s responses from reactivity to creativity.</p>
  <p class="body-copy copy-experience">With many years’ experience in coaching and mentorship, mediation and narrative processes, Norah supports you to uncover unique responses to difficult situations.</p>
  <p class="tags tags-back"># consultations &nbsp;# workshops &nbsp;# speaking &nbsp;# articles</p>
  <div class="credential-box">
    <p class="name">Norah <b>Ashford</b></p>
    <p class="quals">PhD, MCR, BAppSci, DipHum, AssDipEd</p>
  </div>
  <address class="contact" style="font-style:normal">
    0400 555 182 (m), &nbsp;+61 3 5550 4417 (h)<br>
    norah@norahashford.com, &nbsp;norahashford.com<br>
    ABN 00 000 000 00
  </address>
</section>

</body>
</html>
```